Corporate Business Card

Very professional, Modern, Not to busy, include phone address email, website
(253) 555-0174, 61807 19th Street N, Kent, WA 98517, marcus@kestrelbayholding.com, brelvanindustries.com

Target Market(s)

Manufacturing

Industry/Entity Type

Aero, machining, manufacturing, Off road racing

Contact Information for Business Card

Phone, address email, website

```html
<!DOCTYPE html>
<html lang="en">
<head>
<meta charset="utf-8">
<title>Brelvan Industries – Business Card</title>
<link rel="stylesheet" href="https://fonts.googleapis.com/css2?family=Open+Sans:wght@400;600&display=swap">
<style>
  :root {
    --brand-navy: #304472;
    --card-white: #ffffff;
    --ink: #333333;
  }
  * { box-sizing: border-box; margin: 0; padding: 0; }
  html, body {
    width: 1200px;
    height: 682px;
    overflow: hidden;
    background: var(--card-white);
  }
  .business-card {
    position: relative;
    width: 1200px;
    height: 682px;
    background: var(--card-white);
    font-family: "Open Sans", sans-serif;
    color: var(--ink);
  }
  .header-band {
    position: absolute;
    left: 0;
    top: 0;
    width: 1200px;
    height: 288px;
    background: var(--brand-navy);
  }
  .company-name {
    position: absolute;
    left: 130px;
    top: 128px;
    font-size: 48px;
    font-weight: 600;
    line-height: 1;
    color: var(--card-white);
    letter-spacing: 0.5px;
  }
  .contact-list {
    position: absolute;
    left: 590px;
    top: 396px;
    list-style: none;
  }
  .contact-item {
    display: flex;
    align-items: flex-start;
    font-size: 32px;
    line-height: 45px;
    white-space: nowrap;
  }
  .contact-icon {
    flex: 0 0 36px;
    width: 36px;
    height: 45px;
    margin-right: 26px;
    display: flex;
    align-items: center;
    justify-content: center;
  }
  .contact-icon svg { fill: var(--ink); }
  .contact-text { display: block; }
</style>
</head>
<body>
  <main class="business-card">
    <header class="header-band">
      <div class="company-name">Brelvan Industries</div>
    </header>

    <ul class="contact-list">
      <li class="contact-item">
        <span class="contact-icon">
          <svg width="16" height="22" viewBox="0 0 16 22" aria-hidden="true">
            <rect x="0" y="0" width="16" height="22" rx="2.5"/>
            <rect x="2" y="3.5" width="12" height="14" fill="#fff"/>
            <circle cx="8" cy="19.7" r="1" fill="#fff"/>
          </svg>
        </span>
        <span class="contact-text">(253) 555-0174</span>
      </li>
      <li class="contact-item">
        <span class="contact-icon">
          <svg width="20" height="26" viewBox="0 0 20 26" aria-hidden="true">
            <path d="M10 0C4.5 0 0 4.3 0 9.7 0 16.5 10 26 10 26s10-9.5 10-16.3C20 4.3 15.5 0 10 0z"/>
            <circle cx="10" cy="9.6" r="4" fill="#fff"/>
          </svg>
        </span>
        <span class="contact-text">61807 19th Street N,<br>Kent, WA 98517</span>
      </li>
      <li class="contact-item">
        <span class="contact-icon">
          <svg width="26" height="20" viewBox="0 0 26 20" aria-hidden="true">
            <rect x="0" y="0" width="26" height="20" rx="2"/>
            <path d="M2 3l11 8 11-8" fill="none" stroke="#fff" stroke-width="2"/>
          </svg>
        </span>
        <span class="contact-text">marcus@kestrelbayholding.com</span>
      </li>
      <li class="contact-item">
        <span class="contact-icon">
          <svg width="24" height="24" viewBox="0 0 24 24" aria-hidden="true">
            <circle cx="12" cy="12" r="12"/>
            <ellipse cx="12" cy="12" rx="4.5" ry="11" fill="none" stroke="#fff" stroke-width="1.6"/>
            <line x1="1" y1="12" x2="23" y2="12" stroke="#fff" stroke-width="1.6"/>
          </svg>
        </span>
        <span class="contact-text">brelvanindustries.com</span>
      </li>
    </ul>
  </main>
</body>
</html>
```